Health Coaching Flyer for New Clients

I need a two-sided flyer (3.5" x 8.5" preferred or 5" x 7") to distribute to potential coaching clients. My business name is Talvora Health & Wellness Coaching. My business is focused on helping people with habit changes that contribute to their overall well-being. I would like the design colors to be gender neutral. I would like a small photo of myself near the "my name is Jen" statement. Please feel free to change the logo color to match the design.

Target Market(s)

Adults of all ages.

Font styles to use
Serif

Requirements
Must have
• Emphasize my opening question (found in health coaching brochure - attached).
• Small picture of myself near "my name is Jen" statement.
Should not have
• No light of pastel colors.

```html
<!DOCTYPE html>
<html lang="en">
<head>
<meta charset="utf-8">
<title>Talvora Health &amp; Wellness Coaching – Flyer</title>
<link rel="stylesheet" href="https://fonts.googleapis.com/css2?family=Montserrat:wght@400;500;600;700;800&display=swap">
<style>
  :root{
    --bg:#d9d9d9;
    --paper:#ffffff;
    --ink:#2b2b2b;
    --text:#3a3a3a;
    --grey:#8f9194;
    --bar:#a9abae;
    --band:#2a2a2a;
  }
  *{box-sizing:border-box;margin:0;padding:0}
  html,body{width:786px;height:1200px;overflow:hidden;background:var(--bg)}
  body{font-family:"Montserrat",Arial,sans-serif;color:var(--text);position:relative}
  .panel{position:absolute;top:174px;width:350px;height:852px;background:var(--paper);overflow:hidden;box-shadow:0 6px 18px rgba(0,0,0,.25)}
  .panel--front{left:23px}
  .panel--back{left:413px}

  /* front */
  .brand{position:absolute;top:38px;left:0;width:100%;text-align:center}
  .brand__name{font-weight:800;font-size:38px;letter-spacing:3px;color:var(--ink);line-height:1}
  .brand__tag{display:flex;align-items:center;justify-content:center;gap:6px;margin-top:4px;font-size:9.5px;font-weight:600;letter-spacing:-.2px;color:var(--ink)}
  .brand__tag i{display:inline-block;width:9px;height:9px;background:var(--ink)}
  .hero{position:absolute;top:94px;left:0;width:100%;height:434px;background:linear-gradient(180deg,#f1f3f5 0%,#dfe3e7 35%,#b9c4cf 55%,#e6e8ea 80%,#f4f4f4 100%)}
  .question{position:absolute;top:528px;left:0;width:100%;height:90px;background:var(--band);color:#fff;font-weight:700;font-size:16.5px;line-height:20px;text-align:center;padding-top:14px;letter-spacing:.3px}
  .portrait{position:absolute;top:646px;left:25px;width:100px;height:142px;background:linear-gradient(180deg,#6b4a3c,#b98a72 60%,#7a5a4c);border:2px solid #eee}
  .coach{position:absolute;top:794px;left:23px;width:130px}
  .coach__name{font-weight:700;font-size:12.5px;color:var(--ink);letter-spacing:.3px}
  .coach__role{font-size:7.5px;color:var(--grey)}
  .bio{position:absolute;top:644px;left:160px;width:155px;font-size:8.3px;line-height:10.8px;text-align:justify;color:var(--text)}
  .bio b{font-weight:700;color:var(--ink)}
  .front-foot{position:absolute;bottom:0;left:0;width:100%;height:16px;background:var(--bar)}

  /* back */
  .studio{position:absolute;top:0;left:0;width:100%;height:298px;background:linear-gradient(180deg,#f4f2ee 0%,#e9e5de 45%,#c9a97c 72%,#8a6b4d 100%)}
  .services-title{position:absolute;top:370px;left:0;width:100%;text-align:center;font-weight:700;font-size:17px;line-height:20px;color:var(--ink)}
  .services-title span{display:block;color:var(--grey)}
  .services-title::after{content:"";display:block;width:100px;height:2px;background:var(--ink);margin:6px auto 0}
  .services{position:absolute;top:448px;left:40px;width:280px;list-style:none}
  .services li{display:flex;gap:14px;font-size:9px;line-height:11.5px;font-weight:600;color:var(--ink);margin-bottom:12px;text-align:justify}
  .services svg{flex:none;width:16px;height:16px}
  .note{position:absolute;left:38px;width:280px;font-size:9px;line-height:11.5px;color:var(--text)}
  .note--1{top:657px}.note--2{top:704px}.note--3{top:752px;font-weight:500;color:var(--ink)}
  .signature{position:absolute;top:786px;left:38px;font-weight:700;font-size:12.5px;color:var(--ink)}
  .contact{position:absolute;bottom:0;left:0;width:100%;height:34px;background:var(--bar);display:flex;align-items:center;gap:14px;padding-left:38px;color:#fff}
  .contact__phone{font-weight:700;font-size:13px;display:flex;align-items:center;gap:5px}
  .contact__mail{font-size:7.5px;font-weight:600;display:flex;align-items:center;gap:4px}
</style>
</head>
<body>
  <section class="panel panel--front">
    <header class="brand">
      <div class="brand__name">TALVORA</div>
      <div class="brand__tag">HEALTH &amp; WELLNESS COACHING <i></i></div>
    </header>
    <div class="hero" role="img" aria-label="Photo of three adults doing a yoga bow pose on blue mats in a bright studio, with fresh fruit, a water bottle and a measuring tape"></div>
    <h1 class="question">NEED SUPPORT IN MAKING<br>REAL, LASTING LIFESTYLE AND<br>BEHAVIOR CHANGES?</h1>
    <div class="portrait" role="img" aria-label="Portrait photo of Jen Talvora"></div>
    <div class="coach">
      <div class="coach__name">JEN TALVORA</div>
      <div class="coach__role">Functional Health Coach</div>
    </div>
    <p class="bio"><b>MY NAME IS JEN.</b> I am studying to become a Board-Certified Functional Health Coach. My training involves many science-based practices that improve both our health and how we grow and change as humans. I now have the opportunity to turn that knowledge into practice by coaching actual clients interested in improving their own health and well-being.</p>
    <div class="front-foot"></div>
  </section>

  <section class="panel panel--back">
    <div class="studio" role="img" aria-label="Photo of a yoga class seated cross-legged on mats facing an instructor in a light wooden-floored studio"></div>
    <h2 class="services-title">FUNCTIONAL HEALTH<span>COACHES</span></h2>
    <ul class="services">
      <li><svg viewBox="0 0 16 16"><rect x="1" y="3" width="12" height="12" fill="none" stroke="#555" stroke-width="1.3"/><path d="M4 8l3 3 8-9" fill="none" stroke="#555" stroke-width="1.6"/></svg>Leverage your strengths rather than focus on your weaknesses</li>
      <li><svg viewBox="0 0 16 16"><rect x="1" y="3" width="12" height="12" fill="none" stroke="#555" stroke-width="1.3"/><path d="M4 8l3 3 8-9" fill="none" stroke="#555" stroke-width="1.6"/></svg>Support you in finding your own strategies and motivation for change</li>
      <li><svg viewBox="0 0 16 16"><rect x="1" y="3" width="12" height="12" fill="none" stroke="#555" stroke-width="1.3"/><path d="M4 8l3 3 8-9" fill="none" stroke="#555" stroke-width="1.6"/></svg>Provide a judgment-free zone and support your autonomy</li>
      <li><svg viewBox="0 0 16 16"><rect x="1" y="3" width="12" height="12" fill="none" stroke="#555" stroke-width="1.3"/><path d="M4 8l3 3 8-9" fill="none" stroke="#555" stroke-width="1.6"/></svg>Use an experimental mindset to find and develop sustainable habits</li>
      <li><svg viewBox="0 0 16 16"><rect x="1" y="3" width="12" height="12" fill="none" stroke="#555" stroke-width="1.3"/><path d="M4 8l3 3 8-9" fill="none" stroke="#555" stroke-width="1.6"/></svg>Act as your accountability partner as you reach your unique health goals; whether they be improving sleep, diet, fitness, social connection, or reducing stress.</li>
    </ul>
    <p class="note note--1">I would like to invite you to participate with me as a client as I continue to hone my coaching skills. We can develop a plan and schedule that aligns with your goals.</p>
    <p class="note note--2">As a way to give back to my community, I am offering new clients six free coaching sessions. This is a limited time offer.</p>
    <p class="note note--3">Please contact me. I'm ready to support you as you work to improve your health.</p>
    <div class="signature">Jen Talvora</div>
    <footer class="contact">
      <span class="contact__phone"><svg width="12" height="12" viewBox="0 0 24 24"><path fill="#fff" d="M6.6 10.8a15.1 15.1 0 006.6 6.6l2.2-2.2a1 1 0 011-.25 11.4 11.4 0 003.6.57 1 1 0 011 1V20a1 1 0 01-1 1A17 17 0 013 4a1 1 0 011-1h3.5a1 1 0 011 1c0 1.25.2 2.45.57 3.57a1 1 0 01-.25 1z"/></svg>555-014-2297</span>
      <span class="contact__mail"><svg width="9" height="7" viewBox="0 0 18 14"><rect width="18" height="14" fill="#fff"/><path d="M0 0l9 7 9-7" fill="none" stroke="#a9abae" stroke-width="1.5"/></svg>talvorahwc@example.com</span>
    </footer>
  </section>
</body>
</html>
```